Velmora Grove Club Postcard Design

Need a postcard for this business. Go to velmoragroveclub.com to see the product we are selling. Here's another good postcard you can sample. https://www.rowanpilsbydesign.com/?lightbox=dataItem-qz4tunal
Another one: http://blog.tranquet.com/postcard-examples-from-popular-startups/

```html
<!DOCTYPE html>
<html lang="en">
<head>
<meta charset="UTF-8">
<title>Velmora Grove Club Postcard</title>
<link href="https://fonts.googleapis.com/css2?family=Arimo:wght@400;700&family=Fredoka:wght@700&display=swap" rel="stylesheet">
<style>
  :root {
    --page: #ffffff;
    --frame: #1a1a1a;
    --leaf-light: #a3cf62;
    --leaf-line: #7fc241;
    --leaf-dark: #2d3d06;
    --leaf-mid: #4f7a13;
    --chew-brown: #3d0f0a;
    --chew-warm: #9a5a34;
    --chew-deep: #6e2f1c;
    --text-light: #ffffff;
  }
  html, body {
    margin: 0;
    padding: 0;
    width: 1200px;
    height: 1000px;
    overflow: hidden;
    background: var(--page);
  }
  .canvas {
    position: relative;
    width: 1200px;
    height: 1000px;
    font-family: "Arimo", Arial, sans-serif;
  }
  .backdrop {
    position: absolute;
    inset: 0;
  }
  .headline-block {
    position: absolute;
    left: 90px;
    top: 192px;
    width: 510px;
    text-align: center;
  }
  .kicker {
    margin: 0;
    font-size: 25px;
    line-height: 1.2;
    color: var(--leaf-mid);
  }
  .club-name {
    margin: 6px 0 0;
    font-family: "Fredoka", "Arial Black", sans-serif;
    font-weight: 700;
    font-size: 56px;
    line-height: 1.18;
    letter-spacing: 0.5px;
    white-space: nowrap;
    color: var(--chew-brown);
  }
  .club-rule {
    width: 252px;
    height: 3px;
    margin: 4px auto 0;
    background: var(--leaf-mid);
  }
  .tagline {
    margin: 12px 0 0;
    font-size: 25px;
    line-height: 1.2;
    color: var(--leaf-mid);
  }
  .product-photo {
    position: absolute;
    left: 590px;
    top: 295px;
    width: 390px;
    height: 415px;
    border-radius: 24px;
    background: linear-gradient(150deg, var(--chew-deep) 0%, var(--chew-warm) 55%, #b87a4c 100%);
  }
  .puppy-photo {
    position: absolute;
    left: 930px;
    top: 568px;
    width: 180px;
    height: 296px;
    border-radius: 24px;
    background: linear-gradient(180deg, #1e1a18 0%, #2a2320 55%, #c08a4e 80%, #f1ece4 100%);
  }
  .offer {
    position: absolute;
    left: 120px;
    top: 684px;
    width: 400px;
    text-align: center;
    color: var(--text-light);
  }
  .offer-lead {
    margin: 0;
    font-size: 26px;
  }
  .offer-amount {
    margin: 0;
    font-size: 60px;
    font-weight: 700;
    line-height: 1.05;
  }
  .offer-code {
    margin: 4px 0 0;
    font-size: 24px;
  }
</style>
</head>
<body>
<div class="canvas">
  <svg class="backdrop" width="1200" height="1000" viewBox="0 0 1200 1000" aria-hidden="true">
    <rect class="card" x="74.5" y="123.5" width="1046" height="746" fill="#ffffff" stroke="var(--frame)" stroke-width="1.5"/>
    <path class="wave-right" d="M825,124 C880,210 1060,280 1080,420 C1100,560 1050,690 940,740 C820,790 600,800 500,869 L1120,869 L1120,124 Z" fill="var(--leaf-light)"/>
    <path class="wave-bottom" d="M75,690 C120,640 250,600 380,595 C520,590 610,650 600,720 C590,790 520,830 470,869 L75,869 Z" fill="var(--leaf-dark)"/>
    <g class="accent-lines" fill="none" stroke-linecap="round">
      <path d="M826,118 C812,170 830,230 905,272" stroke="var(--leaf-line)" stroke-width="4"/>
      <path d="M877,212 C950,250 1000,300 1033,355" stroke="var(--leaf-dark)" stroke-width="4"/>
      <path d="M84,672 C120,645 170,622 216,607" stroke="var(--leaf-line)" stroke-width="4"/>
      <path d="M405,602 C470,600 520,612 545,652" stroke="var(--leaf-line)" stroke-width="4"/>
      <path d="M795,747 C840,750 900,745 935,735" stroke="var(--leaf-line)" stroke-width="4"/>
      <path d="M636,782 C680,760 750,758 800,764" stroke="var(--leaf-mid)" stroke-width="4"/>
    </g>
  </svg>

  <div class="headline-block">
    <p class="kicker">Top Quality &amp; Healthy Bully Sticks</p>
    <h1 class="club-name">VELMORA GROVE<br>CLUB</h1>
    <div class="club-rule"></div>
    <p class="tagline">Your Dog Will Beg For More</p>
  </div>

  <div class="product-photo" role="img" aria-label="Photo of three dried beef bully sticks crossed on a white background"></div>
  <div class="puppy-photo" role="img" aria-label="Photo of a tricolour mountain dog puppy sitting"></div>

  <div class="offer">
    <p class="offer-lead">On your first month</p>
    <p class="offer-amount">SAVE 50%</p>
    <p class="offer-code">USE CODE: VELMORAGROVE</p>
  </div>
</div>
</body>
</html>
```